Brochure Design Project

We are a payroll company. We offer a wide variety of products and services:
1. Payroll Processing
2. Employee Direct Deposit
3. Time and attendance
4. HR services
5. Employee Employee Benefits

I'd like to develop a one page template that uses a combination of our logo (attached), colors (attached) and possible a picture. The picture could be shown as an option as it may change based on the product or service.

Target Market(s)

Adults in the United States ages 22-50. Typically these people are accountants, human resource professionals or entrepreneurs. The payroll industry is dominated by 3 large payroll processors, QLM, Wendrafy and Tolvarex. These companies are very impersonal and make it difficult to resolve issues when they arise. We have grown to over 400 clients by being the opposite of the big guys,

Industry/Entity Type

It Company

Font styles to use
Sans Serif

Requirements
Must have
• The brochure can be one or two pages.
Nice to have
• I'll know it when I see it but I can't describe it. I have attached a few brochures that have caught my eye.
Should not have
• No cartoons. No money signs. Hip, new, fresh are words I'd use to describe the winning product. Of the three people I described in my target market, the entrepreneur is the market I'd most like to target.

```html
<!DOCTYPE html>
<html lang="en">
<head>
<meta charset="utf-8">
<title>Cortavi Payroll – Services Brochure</title>
<link rel="stylesheet" href="https://fonts.googleapis.com/css2?family=Open+Sans:wght@400;600;700;800&display=swap">
<style>
  :root {
    --navy: #1f3266;
    --green: #8cc043;
    --grey: #6f6f6f;
    --grey-dark: #4a4a4a;
    --white: #ffffff;
    --canvas: #ececec;
    --ink: #2a3a6e;
  }
  * { margin: 0; padding: 0; box-sizing: border-box; }
  html, body {
    width: 1200px; height: 1000px; overflow: hidden;
    background: var(--canvas);
    font-family: "Open Sans", Arial, sans-serif;
  }
  .brochure {
    position: absolute; left: 40px; top: 105px;
    width: 1120px; height: 790px;
    background: var(--white);
    box-shadow: 0 6px 24px rgba(0,0,0,.18);
    overflow: hidden;
  }
  .brochure-shapes { position: absolute; inset: 0; }
  .brand-header { position: absolute; left: 60px; top: 28px; }
  .brand-name {
    font-weight: 800; font-size: 46px; line-height: 1;
    color: var(--navy); letter-spacing: -0.5px;
  }
  .services-tag {
    display: inline-block; margin-top: 8px; margin-left: 60px;
    background: var(--green); color: var(--white);
    font-weight: 800; font-size: 28px; letter-spacing: 1px;
    padding: 2px 18px; line-height: 1.2;
  }
  .service {
    position: absolute; width: 240px; color: var(--white); text-align: center;
  }
  .service-icon { display: block; margin: 0 auto; }
  .service-title { font-weight: 700; font-size: 17px; margin: 6px 0 8px; }
  .service-text { font-size: 12.5px; line-height: 1.45; text-align: justify; }
  .tagline {
    position: absolute; left: 80px; top: 560px;
    color: var(--white); font-weight: 700; font-size: 38px; line-height: 1;
  }
  .contact { position: absolute; left: 60px; top: 648px; color: var(--navy); font-size: 13px; }
  .contact-phone { display: flex; align-items: center; gap: 8px; font-weight: 700; margin-bottom: 10px; }
  .contact-web { letter-spacing: 1px; }
  .brand-footer {
    position: absolute; right: 60px; top: 708px;
    font-weight: 800; font-size: 40px; color: var(--navy); line-height: 1;
  }
</style>
</head>
<body>
<div class="brochure">
  <svg class="brochure-shapes" width="1120" height="790" viewBox="0 0 1120 790" aria-hidden="true">
    <polygon points="0,150 1120,150 1120,680 480,680 430,620 0,620" fill="var(--navy)"/>
    <polygon points="760,205 1120,205 1120,470" fill="var(--green)"/>
    <polygon points="0,545 400,545 455,620 0,620" fill="var(--grey)"/>
    <polygon points="400,620 455,620 430,650" fill="var(--grey-dark)"/>
    <circle cx="720" cy="235" r="62" fill="var(--white)"/>
    <circle cx="720" cy="235" r="44" fill="none" stroke="var(--navy)" stroke-width="6"/>
    <g fill="none" stroke="var(--white)" stroke-width="2.5" stroke-dasharray="2 5">
      <polyline points="200,125 200,165 160,165 160,190"/>
      <polyline points="160,165 420,165 420,240"/>
      <polyline points="420,165 700,165"/>
      <polyline points="720,297 720,320"/>
      <polyline points="782,235 940,235 940,400"/>
    </g>
    <g fill="var(--white)">
      <circle cx="160" cy="190" r="4"/><circle cx="420" cy="240" r="4"/>
      <circle cx="720" cy="320" r="4"/><circle cx="940" cy="400" r="4"/>
    </g>
  </svg>

  <header class="brand-header">
    <div class="brand-name">Cortavi Payroll</div>
    <div class="services-tag">SERVICES</div>
  </header>

  <section class="service" style="left:40px; top:196px;">
    <svg class="service-icon" width="70" height="60" viewBox="0 0 70 60" aria-hidden="true">
      <rect x="4" y="8" width="60" height="46" rx="6" fill="var(--white)"/>
      <rect x="40" y="22" width="28" height="18" rx="4" fill="var(--navy)"/>
      <circle cx="50" cy="31" r="3" fill="var(--white)"/>
    </svg>
    <h3 class="service-title">Service</h3>
    <p class="service-text">Our Support Services package has been specially designed to provide our clients with a flexible solution that has no "lock in" contract terms. This service package allows for the purchase of block hours that can be utilised at any time and which never expire.</p>
  </section>

  <section class="service" style="left:300px; top:248px;">
    <svg class="service-icon" width="80" height="60" viewBox="0 0 80 60" aria-hidden="true">
      <rect x="4" y="6" width="72" height="48" rx="6" fill="none" stroke="var(--white)" stroke-width="5"/>
      <rect x="4" y="17" width="72" height="8" fill="var(--white)"/>
      <rect x="54" y="34" width="12" height="10" fill="var(--white)"/>
    </svg>
    <h3 class="service-title">Service</h3>
    <p class="service-text">Our Managed Services package is Nexora's outsourcing service and is an excellent way to assist our clients with delivering against all their internal business needs. What makes this particular service unique is it greatly reduces (and often removes) the need for expensive internal resources normally dedicated to maintaining and improving a business's systems.</p>
  </section>

  <section class="service" style="left:560px; top:328px;">
    <svg class="service-icon" width="70" height="60" viewBox="0 0 70 60" aria-hidden="true">
      <rect x="24" y="4" width="22" height="12" rx="3" fill="none" stroke="var(--white)" stroke-width="5"/>
      <rect x="4" y="14" width="62" height="42" rx="5" fill="var(--white)"/>
      <rect x="4" y="30" width="62" height="4" fill="var(--navy)"/>
      <rect x="31" y="27" width="8" height="10" fill="var(--white)" stroke="var(--navy)" stroke-width="2"/>
    </svg>
    <h3 class="service-title">Service</h3>
    <p class="service-text">Our Consulting Services is an excellent way for our clients to access the expert skills and years of knowledge held with our engineers. This expertise is most commonly used for small, medium and large project works, to bridge implementation knowledge gaps and/or to assist with the strategic planning of solutions.</p>
  </section>

  <section class="service" style="left:820px; top:408px;">
    <svg class="service-icon" width="60" height="70" viewBox="0 0 60 70" aria-hidden="true">
      <rect x="6" y="4" width="48" height="62" fill="none" stroke="var(--white)" stroke-width="5"/>
      <g fill="var(--white)">
        <rect x="14" y="12" width="7" height="7"/><rect x="27" y="12" width="7" height="7"/><rect x="40" y="12" width="7" height="7"/>
        <rect x="14" y="25" width="7" height="7"/><rect x="27" y="25" width="7" height="7"/><rect x="40" y="25" width="7" height="7"/>
        <rect x="14" y="38" width="7" height="7"/><rect x="27" y="38" width="7" height="7"/><rect x="40" y="38" width="7" height="7"/>
        <rect x="25" y="52" width="11" height="14"/>
      </g>
    </svg>
    <h3 class="service-title">Service</h3>
    <p class="service-text">Is your current solution too expensive, outdated, hard to understand or a huge drain on your internal resources? Do you want to remove the headache of dealing with the day to day management that goes with maintaining a system? Then Nexora's fully hosted services may be the perfect fit for your business.</p>
  </section>

  <div class="tagline">a Payroll Partner.</div>

  <div class="contact">
    <div class="contact-phone">
      <svg width="16" height="16" viewBox="0 0 16 16" aria-hidden="true">
        <rect width="16" height="16" rx="3" fill="var(--navy)"/>
        <path d="M5 3.5c.6 0 1 1.6 1 2.2 0 .5-.8.7-.6 1.3.4 1 1.3 1.9 2.3 2.3.6.2.8-.6 1.3-.6.6 0 2.2.4 2.2 1s-.9 2-2 1.8C6.4 11 4.9 9.5 4.4 6.3 4.2 5 4.5 3.5 5 3.5z" fill="var(--white)"/>
      </svg>
      1300 555 018
    </div>
    <div class="contact-web">www.cortavipayroll.com</div>
  </div>

  <div class="brand-footer">Cortavi Payroll</div>
</div>
</body>
</html>
```